Corporate Brightfen business cards to be handed to investor, bankers etc. Needs to have a young feel

I need business cards designed for a technology company that provides uber-like rapid response on the security industry. I would like it simple but very cool and tasteful. See attached documents for artwork and colours to be used. Cut sheet describes business model. Card stock should be thicker than normal. I would like the one side to be just the art and the other to have the contact info with maybe the pin somewhere.

Target Market(s)

Investors

Industry/Entity Type

Business

Contact Information for Business Card

Would like the logo attached on one side with name address and other info on the other side.

Font styles to use
Other font styles liked:
• See existing logo

Colors
6b449b
886aae
e4daeb
ffffff

Requirements
Must have
• Name: Dorian Felkatsis
• Address: 47 Larkfield Avenue, Toronto, On, M6K2B7
• Tel: 416-7291846
• Email: rolo@brightfen.io
Nice to have
• See logo colours

```html
<!DOCTYPE html>
<html lang="en">
<head>
<meta charset="utf-8">
<title>Brightfen Business Cards</title>
<link href="https://fonts.googleapis.com/css2?family=Lato:wght@300;400;700&display=swap" rel="stylesheet">
<style>
  :root {
    --brand-purple: #6b449b;
    --brand-purple-soft: #886aae;
    --brand-lilac: #e4daeb;
    --white: #ffffff;
    --ink: #1a1a1a;
    --text-grey: #8c8c8c;
    --backdrop: #d9d9db;
  }
  * { margin: 0; padding: 0; box-sizing: border-box; }
  html, body {
    width: 1200px; height: 1000px; overflow: hidden;
    background: var(--backdrop);
    font-family: "Lato", Arial, sans-serif;
  }
  .canvas { position: relative; width: 1200px; height: 1000px; }

  .card {
    position: absolute; left: 269px; width: 662px; height: 378px;
    box-shadow: 0 4px 10px rgba(0,0,0,0.25);
    overflow: hidden;
  }
  .card-front { top: 108px; background: var(--white); }
  .card-back { top: 522px; background: var(--brand-purple); }

  .wordmark {
    position: absolute; display: flex; align-items: center;
    font-weight: 300; letter-spacing: -0.5px; line-height: 1;
  }
  .wordmark-dot { border-radius: 50%; flex: none; }
  .card-front .wordmark { left: 51px; top: 82px; font-size: 58px; color: var(--ink); }
  .card-front .wordmark-dot { width: 20px; height: 20px; background: var(--brand-purple); margin-right: 8px; margin-top: 6px; }
  .card-back .wordmark { left: 0; right: 0; justify-content: center; top: 146px; font-size: 74px; color: var(--white); }
  .card-back .wordmark-dot { width: 26px; height: 26px; background: var(--white); margin-right: 12px; margin-top: 8px; }

  .contact { position: absolute; left: 360px; top: 86px; right: 0; color: var(--text-grey); font-size: 17px; line-height: 22px; }
  .contact-name { color: var(--brand-purple); font-size: 22px; font-weight: 700; line-height: 26px; }
  .contact-title { margin-top: 1px; }
  .contact-rule { height: 2px; background: var(--brand-purple); margin-top: 16px; margin-bottom: 17px; }
  .contact-address { margin-bottom: 9px; }
  .label { color: var(--brand-purple); font-weight: 700; }
  .accent { color: var(--brand-purple); }

  .back-decor { position: absolute; left: 340px; top: 10px; width: 440px; height: 440px; }
  .back-url {
    position: absolute; left: 0; right: 0; bottom: 32px; text-align: center;
    color: var(--white); font-size: 14px;
  }
</style>
</head>
<body>
<main class="canvas">
  <section class="card card-front" aria-label="Business card front">
    <div class="wordmark"><span class="wordmark-dot"></span>brightfen</div>
    <div class="contact">
      <p class="contact-name">Dorian Felkatsis</p>
      <p class="contact-title">President</p>
      <div class="contact-rule"></div>
      <p class="contact-address">47 Larkfield Avenue, Toronto,<br>On, M6K2B7</p>
      <p><span class="label">T</span>: 416-7291846</p>
      <p><span class="label">E</span>: rolo@brightfen.io</p>
      <p>www.<span class="accent">brightfen</span>.io</p>
    </div>
  </section>

  <section class="card card-back" aria-label="Business card back">
    <svg class="back-decor" viewBox="0 0 440 440" aria-hidden="true">
      <circle cx="220" cy="220" r="220" fill="#5f3b8f" opacity="0.45"/>
    </svg>
    <div class="wordmark"><span class="wordmark-dot"></span>brightfen</div>
    <p class="back-url">www.brightfen.io</p>
  </section>
</main>
</body>
</html>
```